Update existing website to a one page design.

Combine a multi page website into a single page design.
Existing site is at ac.calmharborcover (dot) com.
Rearrange elements as needed to create a modem look.
Not every element / all of the text need to be kept, design should be flexible enough to allow for new text (of different length) to be used.
Site should have a clear calls to action, such as get a quote and contact us.
Ability, call to action, to switch to Russian should be clearly visible near the top, translation will not be done by google, thus attribution is not needed.
Unused features (such as blog) should be dropped.
Images, besides logos, can be brand new.
Site should adhere to standard design practices (such as grid) and ideally be compatible with existing framework (such as bootstrap).
Coding of the website will likely be done by the winning bidder as a separate project.

```html
<!DOCTYPE html>
<html lang="en">
<head>
<meta charset="utf-8">
<title>Calm Harbor Cover</title>
<link href="https://fonts.googleapis.com/css2?family=Poppins:wght@300;400;500;600;700&display=swap" rel="stylesheet">
<style>
:root{
  --blue:#1d4fae;
  --blue-dark:#163f8f;
  --ink:#1d1d1f;
  --text:#4a4a4a;
  --grey-bg:#f3f3f3;
  --services:#3f3f3f;
  --cta:#2a2d33;
  --footer:#1e2230;
  --white:#ffffff;
}
*{box-sizing:border-box;margin:0;padding:0}
html,body{width:1200px;height:3692px;overflow:hidden}
body{font-family:"Poppins",sans-serif;color:var(--ink);background:var(--white);position:relative}
.abs{position:absolute}
.btn{display:inline-block;background:var(--blue);color:var(--white);font-size:13px;font-weight:600;letter-spacing:.5px;padding:10px 26px;border-radius:22px;text-transform:uppercase;white-space:nowrap}
.btn-light{background:var(--white);color:var(--blue)}

/* header */
.site-header{top:0;left:0;width:1200px;height:48px;background:var(--white);z-index:3}
.brand{top:0;left:160px;width:88px;height:96px;background:var(--blue);color:var(--white);display:flex;flex-direction:column;align-items:center;justify-content:center;gap:6px;z-index:4;font-weight:700;font-size:13px;text-align:center;line-height:1.1;text-transform:uppercase}
.brand .mark{width:26px;height:26px;background:var(--white);border-radius:50%}
.main-nav{top:0;right:120px;height:48px;display:flex;align-items:center;gap:28px;font-size:14px;color:var(--ink);white-space:nowrap}
.main-nav .btn{padding:7px 18px;font-size:12px;text-transform:none}
.lang-switch{display:flex;align-items:center;border:1.5px solid var(--blue);border-radius:16px;overflow:hidden;font-size:12px;font-weight:600}
.lang-switch span{padding:5px 11px;color:var(--blue)}
.lang-switch .active{background:var(--blue);color:var(--white)}

/* hero */
.hero{top:48px;left:0;width:1200px;height:580px;background:linear-gradient(100deg,#5b6b4f 0%,#8a9a72 40%,#c9cbb8 70%,#e7e4da 100%)}
.hero-text{top:236px;left:192px;color:var(--white);width:460px}
.hero-text .kicker{font-size:30px;font-weight:600}
.hero-text h1{font-size:40px;font-weight:700;line-height:1.2;margin-top:4px}
.hero-text p{font-size:17px;line-height:1.6;margin-top:18px}
.hero-text .btn{margin-top:24px}
.slider-arrow{top:310px;width:40px;height:40px;border-radius:50%;background:rgba(0,0,0,.45);display:flex;align-items:center;justify-content:center}

/* about */
.about-bg{top:620px;left:0;width:1200px;height:610px;background:var(--grey-bg)}
.about-photo{top:780px;left:180px;width:380px;height:380px;border-radius:50%;background:linear-gradient(135deg,#c7ab8f,#f2e6da 60%,#e9ecef);border:10px solid var(--white)}
.about-circle{top:900px;left:130px;width:200px;height:200px;border-radius:50%;background:#e3e3e3}
.about-text{top:790px;left:688px;width:340px}
.about-text h2{font-size:28px;font-weight:600}
.about-text .lead{font-size:13px;font-weight:600;line-height:1.6;margin-top:18px}
.about-text p{font-size:12px;line-height:1.7;color:var(--text);margin-top:14px}
.about-text .btn{margin-top:26px}

/* doctor */
.doctor-photo{top:1228px;left:0;width:1200px;height:500px;background:linear-gradient(90deg,#d8c6b4,#f0e2d2 50%,#c8b49b)}
.doctor-text{top:1420px;left:192px;color:var(--white);width:320px}
.doctor-text h2{font-size:36px;font-weight:700}
.doctor-text p{font-size:14px;line-height:1.6;margin-top:12px}
.doctor-text .btn{margin-top:22px}

/* services */
.services{top:1728px;left:0;width:1200px;height:532px;background:var(--services);color:var(--white);text-align:center}
.services h2{position:absolute;top:80px;left:0;width:1200px;font-size:52px;font-weight:300}
.services h2 b{font-weight:600}
.service-list{position:absolute;top:190px;left:230px;width:760px;display:flex;justify-content:space-between;text-align:left}
.service{width:230px}
.service svg{display:block;margin:0 0 16px 16px}
.service h3{font-size:14px;font-weight:600;letter-spacing:.3px}
.service p{font-size:12px;line-height:1.6;opacity:.85;margin-top:6px}
.services .btn{position:absolute;top:420px;left:525px}

/* individual */
.family{top:2260px;left:0;width:1200px;height:660px;background:linear-gradient(180deg,#f4f4f2,#e9e8e4 60%,#d7d2c8)}
.family-text{top:2370px;left:0;width:1200px;text-align:center}
.family-text h2{font-size:34px;font-weight:700}
.family-text p{font-size:17px;margin-top:6px;color:var(--text)}
.family-text .btn{margin-top:36px}

/* testimonials */
.testimonials{top:2920px;left:0;width:1200px;height:328px;background:linear-gradient(90deg,var(--blue-dark),var(--blue))}
.quote-card{top:2980px;width:340px;height:160px;background:var(--white);padding:26px 26px 26px 62px}
.quote-card::before{content:"\201C";position:absolute;left:22px;top:10px;font-size:56px;color:var(--blue);font-weight:700}
.quote-card p{font-size:13px;line-height:1.6;color:var(--text)}
.author{top:3150px;display:flex;align-items:center;gap:14px;color:var(--white)}
.author .avatar{width:42px;height:42px;border-radius:50%;background:#c9b39c}
.author b{display:block;font-size:12px}
.author span{font-size:11px;opacity:.8}
.dots{top:3208px;left:580px;display:flex;gap:8px}
.dots i{width:8px;height:8px;border-radius:50%;background:rgba(255,255,255,.45)}
.dots i:first-child{background:var(--white)}

/* cta */
.cta{top:3248px;left:0;width:1200px;height:112px;background:var(--cta);color:var(--white)}
.cta-text{position:absolute;top:34px;left:260px}
.cta-text .q{font-size:17px}
.cta-text b{font-size:14px;font-weight:600;display:block;margin-top:2px}
.cta .btn{position:absolute;top:36px;left:820px;border-radius:4px;font-size:12px}

/* footer */
.site-footer{top:3360px;left:0;width:1200px;height:332px;background:var(--footer);color:#c9ccd6}
.footer-brand{position:absolute;top:60px;left:240px;width:80px;height:96px;background:var(--blue);color:var(--white);display:flex;flex-direction:column;align-items:center;justify-content:center;gap:6px;font-weight:700;font-size:12px;text-align:center;text-transform:uppercase;line-height:1.1}
.footer-brand .mark{width:24px;height:24px;background:var(--white);border-radius:50%}
.footer-col{position:absolute;top:60px}
.footer-col h4{color:var(--white);font-size:14px;font-weight:600;margin-bottom:14px}
.footer-col li{list-style:none;font-size:12px;line-height:1.9}
.social{display:flex;gap:8px}
.social i{width:26px;height:26px;border-radius:50%;background:var(--blue)}
.newsletter{display:flex;margin-top:8px}
.newsletter span{width:120px;height:28px;background:var(--white);font-size:11px;color:#888;padding:6px 8px}
.newsletter b{width:28px;height:28px;background:var(--blue);display:flex;align-items:center;justify-content:center}
.footer-bottom{position:absolute;top:262px;left:240px;width:720px;border-top:1px solid #39405a;padding-top:18px;font-size:11px;display:flex;justify-content:space-between}
</style>
</head>
<body>

<header class="abs site-header">
  <nav class="abs main-nav">
    <span>Home</span><span>Insurance</span><span>Property &amp; Commercial</span><span>Doctors</span><span>Contact Us</span>
    <span class="lang-switch"><span class="active">EN</span><span>RU</span></span>
    <span class="btn">Get A Quote</span>
  </nav>
</header>
<div class="abs brand"><span class="mark"></span>Calm<br>Harbor</div>

<section class="abs hero" role="img" aria-label="Family relaxing together outdoors on a sunny lawn"></section>
<svg class="abs" style="top:520px;left:0" width="1200" height="110" viewBox="0 0 1200 110" preserveAspectRatio="none"><path d="M0 80Q600 70 1200 10V30Q600 90 0 110Z" fill="#fff"/><path d="M0 110Q600 90 1200 30V110Z" fill="#f3f3f3"/></svg>
<div class="abs hero-text">
  <div class="kicker">Calm Harbor Cover</div>
  <h1>Calm Harbor Cover Corporation</h1>
  <p>Calm Harbor Cover Corporation is an Independent Insurance and Financial Brokerage Firm</p>
  <span class="btn">Quote Now</span>
</div>
<span class="abs slider-arrow" style="left:48px"><svg width="14" height="14" viewBox="0 0 14 14"><path d="M9 2 4 7l5 5" stroke="#fff" stroke-width="2" fill="none"/></svg></span>
<span class="abs slider-arrow" style="left:1112px"><svg width="14" height="14" viewBox="0 0 14 14"><path d="M5 2l5 5-5 5" stroke="#fff" stroke-width="2" fill="none"/></svg></span>

<div class="abs about-bg"></div>
<div class="abs about-circle"></div>
<div class="abs about-photo" role="img" aria-label="Couple reviewing insurance papers with an advisor"></div>
<div class="abs about-text">
  <h2>Calm Harbor Cover</h2>
  <p class="lead">Calm Harbor Cover Corporation is an Independent Insurance and Financial Brokerage Firm serving clients throughout Florida and internationally.</p>
  <p>We are an experienced team of professionals, committed to our primary mission – to find the best available insurance coverage, for protection you need, at the best rate you deserve. Our integrated suite of offers allows us to tailor a comprehensive plan to meet needs of leading insurance companies.</p>
  <span class="btn">Learn More</span>
</div>

<div class="abs doctor-photo" role="img" aria-label="Smiling family of three at home"></div>
<svg class="abs" style="top:1228px;left:0" width="1200" height="500" viewBox="0 0 1200 500"><path d="M0 0H560Q700 250 560 500H0Z" fill="#1d4fae"/></svg>
<div class="abs doctor-text">
  <h2>FIND A DOCTOR</h2>
  <p>Click here to find a provider or hospital under the insurance company you prefer</p>
  <span class="btn btn-light">Learn More</span>
</div>

<section class="abs services">
  <h2>Services <b>We Offer</b></h2>
  <div class="service-list">
    <div class="service">
      <svg width="44" height="40" viewBox="0 0 44 40" fill="none" stroke="#fff" stroke-width="2"><path d="M22 36 6 20a9 9 0 0 1 16-10 9 9 0 0 1 16 10Z"/><path d="M14 22h16M22 14v16"/></svg>
      <h3>COMMERCIAL INSURANCE</h3>
      <p>Lorem ipsum dolor sit amet elit. Mauris in rhoncus orci, nulla sed facilisis accumsan dui.</p>
    </div>
    <div class="service">
      <svg width="44" height="40" viewBox="0 0 44 40" fill="none" stroke="#fff" stroke-width="2"><path d="M12 6c4-2 8 2 10 2s6-4 10-2 4 10 2 16-3 14-6 14-3-10-6-10-3 10-6 10-4-8-6-14-2-14 2-16Z"/></svg>
      <h3>DENTAL INSURANCE</h3>
      <p>Lorem ipsum dolor sit amet elit. Mauris in rhoncus orci, nulla sed facilisis accumsan dui.</p>
    </div>
    <div class="service">
      <svg width="44" height="40" viewBox="0 0 44 40" fill="none" stroke="#fff" stroke-width="2"><path d="M4 20a18 16 0 0 1 36 0Z"/><path d="M22 20v12a4 4 0 0 1-8 0"/><path d="M22 4V2"/></svg>
      <h3>GROUP HEALTH INSURANCE</h3>
      <p>Lorem ipsum dolor sit amet elit. Mauris in rhoncus orci, nulla sed facilisis accumsan dui.</p>
    </div>
  </div>
  <span class="btn btn-light">More Services</span>
</section>

<section class="abs family" role="img" aria-label="Couple relaxing on a white sofa in a bright living room"></section>
<div class="abs family-text">
  <h2>Individual/Family Health Insurance</h2>
  <p>Do not wait for telephone attendant any more!</p>
  <span class="btn">Learn More</span>
</div>

<section class="abs testimonials"></section>
<div class="abs quote-card" style="left:240px"><p>The helpful team got me covered fast and was so easy to deal with. I found the right plan for my family in one short call.</p></div>
<div class="abs quote-card" style="left:640px"><p>The helpful team got me covered fast and was so easy to deal with. I found the right plan for my family in one short call.</p></div>
<div class="abs author" style="left:256px"><span class="avatar" role="img" aria-label="Client portrait"></span><div><b>MIA RAY</b><span>Senior client manager</span></div></div>
<div class="abs author" style="left:656px"><span class="avatar" role="img" aria-label="Client portrait"></span><div><b>OWEN LYLE</b><span>Senior client manager</span></div></div>
<div class="abs dots"><i></i><i></i><i></i></div>

<section class="abs cta">
  <div class="cta-text"><span class="q">Have any question or</span><b>The Best Health Plans for You and Your Family</b></div>
  <span class="btn">Contact Us Now</span>
</section>

<footer class="abs site-footer">
  <div class="footer-brand"><span class="mark"></span>Calm<br>Harbor</div>
  <div class="footer-col" style="left:420px">
    <h4>Site Links</h4>
    <ul><li>Home</li><li>Individual Health</li><li>Group Health</li><li>Life Insurance</li><li>Dental &amp; Vision</li></ul>
  </div>
  <div class="footer-col" style="left:620px">
    <h4>Site Links</h4>
    <ul><li>Property &amp; Commercial</li><li>Doctors Network</li><li>Enrolling</li><li>Get an Instant Quote</li><li>Contact Us</li></ul>
  </div>
  <div class="footer-col" style="left:860px">
    <h4>Get Connected</h4>
    <div class="social"><i></i><i></i><i></i></div>
    <h4 style="margin-top:22px">Newsletter</h4>
    <div class="newsletter"><span>Email</span><b><svg width="12" height="12" viewBox="0 0 12 12"><path d="M1 6h9M6 2l4 4-4 4" stroke="#fff" stroke-width="1.8" fill="none"/></svg></b></div>
  </div>
  <div class="footer-bottom"><span>©2019 Calm Harbor Cover | All Rights Reserved</span><span>Terms &amp; Conditions | Privacy Policy</span></div>
</footer>

</body>
</html>
```